Vielen Dank für die tolle, schnelle Zusammenarbeit und den sympathischen Austausch!
Zielgruppe
Die Energie steckt in Dir!
Wer kennt ihn nicht diesen Punkt, an dem man merkt, es passt nicht mehr, die innerliche Freude, unsere schwungrad für das berufliche Tun ist weg. Es muss sich etwas ändern, doch wir wissen nicht wie. Verschiedene Dinge haben wir bereits ausprobiert, doch wir kommen nicht weiter.
Gut, wenn man einen unabhängigen und verschwiegenen Sparringspartner hat, bei dem man, das was einen beschäftigt, frei äußern darf, sein Gedanken-Karussell sortieren kann und der einen unterstützt, das eigene Ziel zu erreichen.
Die Energie steckt in Ihrem Unternehmen!
In der heutigen Zeit sind wir vielen internen und externen Einflüssen ausgesetzt (Digitalisierung, Änderung der Kundenwünsche, Führungswechsel, u.a.), die die Zusammenarbeit, Kommunikation und das Führungsverhalten im Unternehmen stark beeinflussen und die uns zwingen neue Wege zu gehen. Wollen wir weiterhin erfolgreich sein, müssen wir uns als Team an einen Tisch setzen und gemeinsam Planen, wie wir mit diesen Veränderungen umgehen und wie die Zukunft aussehen könnte.
Als Schwungrad-Lotsin begleite ich erfolgreiche Frauen (weibliche Fach- und Führungskräfte) und Teams in Veränderungsprozessen.
Ich lade sie ein, diesen Prozess AKTIV MITZUGESTALTEN, Ihr Umfeld einzubeziehen und KLAR und WERTSCHÄTZEND zu KOMMUNIZIEREN. Für mehr innere Balance. Für MEHR SCHWUNGRAD am beruflichen Tun.
Ich bin davon überzeugt, alles Wissen und Energie in uns Menschen vorhanden ist, um Ziele erfolgreich zu meistern. Ich helfe Menschen und Teams, dieses Wissen/Wünsche freizusetzen, sie zu kommunizieren und ins Tun zu kommen.
Mein Angebot: Impuls-Coaching, Impuls-Seminare, Impuls-Workshops (World Café) rund um die Themen Veränderung, Kommunikation und Führung. Meine Konzept sind individuell auf die Einzelperson/ Unternehmen zugeschnitten (tailor-made).
Aufgabenstellung
Neue Infos:
Bild im Logo: eher abstrakt Richtung Energiewirbel o.ä., kein Tier, Blume o.ä.
Das Logo soll meinen Namen enthalten. Wahlweise Die Schwungrad-Lotsin, Impulse-Seminare, - Workshops & -Coaching, Die Energie steckt in Dir!. Für andere Zusammenstellung/ Ideen bin ich offen.
Ich könnte mir gut vorstellen, dass auf der Rückseite der Visitenkarte in einer Art Lexikoneintrag der Begriff „Schwungrad-Lotsin“ erklärt wird (siehe Beispiel anbei). Meine aktuelle Visitenkarte – Elemente/ der Schriftzug können übernommen werden, müssen aber nicht. Gut hat mir bisher auch das Foto auf der Rückseite gefallen.
Als Trainerin arbeite ich viel mit Powerpoint, daher wäre es schön, wenn (Teile der) die Elemente des Logos/ Corporate Design so gestaltet sind, dass sie sich für den Master einer Powerpoint „eignen“ bzw. sich dort mit wenig Platzaufwand widerspiegeln.
Der Briefbogen wird zu 90% digital verwendet.Einbinden des KPRF-Logos. Ggf. offenes Word-Dokument, so dass ich selbst etwas verändern kann.
Das Design an sich soll authentisch, klar, auf den Punkt, aktiv/begeisternd/dynamisch, wertvoll sein.
Bildsprache Frauen, Freude, Energie, Wohlfühlen. Veränderung.
Als Farben frisches, sattes Orange, dunkles grau (siehe Visitenkarte anbei).
Schrift klare, ggf. schwungvolle Schrift, aber nicht verschnörkelt.

```html
<!DOCTYPE html>
<html lang="de">
<head>
<meta charset="utf-8">
<title>Carola Wendtke – Die Schwungrad-Lotsin</title>
<link href="https://fonts.googleapis.com/css2?family=Open+Sans:wght@400;600;700&display=swap" rel="stylesheet">
<style>
  :root {
    --orange: #ec8a14;
    --grey-dark: #5a5a5a;
    --grey-text: #444;
    --grey-light: #9a9a9a;
    --stage: #dfe2e9;
    --paper: #ffffff;
    --decor-tone: #eeeff2;
  }
  * { box-sizing: border-box; margin: 0; padding: 0; }
  html, body { width: 878px; height: 1200px; overflow: hidden; }
  body { position: relative; background: var(--paper); font-family: "Open Sans", Arial, sans-serif; color: var(--grey-text); }

  /* brand header */
  .brand { position: absolute; left: 0; top: 0; width: 878px; height: 496px; background: var(--paper); }
  .brand-mark { position: absolute; left: 357px; top: 105px; width: 164px; height: 164px; border-radius: 50%; border: 10px solid var(--orange); }
  .brand-name { position: absolute; left: 0; width: 878px; top: 292px; text-align: center; font-size: 70px; font-weight: 600; color: var(--orange); letter-spacing: 1px; line-height: 1; }
  .brand-tagline { position: absolute; left: 0; width: 878px; top: 381px; text-align: center; font-size: 22px; font-weight: 400; color: var(--grey-dark); letter-spacing: 3.5px; text-transform: uppercase; }

  /* stationery stage */
  .stage { position: absolute; left: 0; top: 496px; width: 878px; height: 704px; background: var(--stage); }

  .sheet { position: absolute; width: 441px; height: 623px; background: var(--paper); box-shadow: 3px 4px 6px rgba(0,0,0,0.12); overflow: hidden; }
  .sheet--main { left: 106px; top: 55px; }
  .sheet--small { left: 573px; top: 148px; transform: scale(0.535); transform-origin: 0 0; }

  /* flat placeholder for the background decoration */
  .sheet-decor { position: absolute; left: 0; top: 210px; width: 441px; height: 413px;
    background: linear-gradient(180deg, rgba(238,239,242,0) 0%, var(--decor-tone) 100%); }

  .sheet-mark { position: absolute; left: 308px; top: 37px; width: 28px; height: 28px; border-radius: 50%; border: 2px solid var(--orange); }
  .sheet-name { position: absolute; left: 240px; width: 168px; top: 71px; text-align: center; font-size: 15px; font-weight: 600; color: var(--orange); line-height: 1; }
  .sheet-tagline { position: absolute; left: 240px; width: 168px; top: 89px; text-align: center; font-size: 5.4px; letter-spacing: 1px; color: var(--grey-dark); text-transform: uppercase; }

  .sender { position: absolute; left: 61px; top: 96px; font-size: 5px; color: var(--grey-light); }
  .recipient { position: absolute; left: 61px; top: 113px; font-size: 7px; line-height: 8.6px; }
  .contact { position: absolute; right: 59px; top: 160px; font-size: 7px; line-height: 8.6px; text-align: right; }
  .date { position: absolute; right: 59px; top: 196px; font-size: 7px; }
  .fold { position: absolute; left: 7px; width: 11px; height: 0; border-top: 0.6px solid #b5b5b5; }
  .fold--one { top: 221px; }
  .fold--two { top: 311px; }

  .subject { position: absolute; left: 61px; top: 231px; font-size: 7.4px; font-weight: 700; color: var(--orange); }
  .body { position: absolute; left: 61px; top: 252px; width: 324px; font-size: 7.2px; line-height: 8.5px; }
  .body p { margin-bottom: 8.5px; }
  .signature { display: block; width: 120px; height: 28px; margin-top: 2px; background: linear-gradient(90deg, rgba(90,90,90,0.18), rgba(90,90,90,0.05)); border-radius: 3px; }

  .footer { position: absolute; left: 0; width: 441px; top: 591px; text-align: center; font-size: 5.3px; line-height: 6.6px; color: var(--grey-dark); }
</style>
</head>
<body>

<header class="brand">
  <div class="brand-mark"></div>
  <div class="brand-name">Carola Wendtke</div>
  <div class="brand-tagline">Die Schwungrad-Lotsin</div>
</header>

<section class="stage">

  <article class="sheet sheet--main">
    <div class="sheet-decor" role="img" aria-label="Faint grey background decoration area"></div>
    <div class="sheet-mark"></div>
    <div class="sheet-name">Carola Wendtke</div>
    <div class="sheet-tagline">Die Schwungrad-Lotsin</div>

    <div class="sender">Carola Wendtke | Lindenhofweg 14 | 45127 Essen</div>
    <div class="recipient">Muster GmbH<br>Herrn Max Mustermann<br>Mustergasse 12<br>44567 Musterdorf<br>Musterhausen</div>
    <div class="contact">Mobil 0171 / 48 6 21 07<br>schwungrad@carola-wendtke.de<br>Steuernummer: xxx/xxxx/xxxx</div>
    <div class="date">Essen, 19. Mai 2017</div>
    <span class="fold fold--one"></span>
    <span class="fold fold--two"></span>

    <div class="subject">Hier ist Platz für den Betreff</div>
    <div class="body">
      <p>Sehr geehrte Damen und Herren,</p>
      <p>Lorem ipsum dolor sit amet, consectetuer adipiscing elit. Aenean commodo ligula eget dolor. Aenean massa. Cum sociis natoque penatibus et magnis dis parturient montes, nascetur ridiculus mus. Donec quam felis, ultricies nec, pellentesque eu, pretium quis, sem. Nulla consequat massa quis enim. Donec pede justo, fringilla vel, aliquet nec, vulputate eget, arcu. In enim justo, rhoncus ut, imperdiet a, venenatis vitae, justo.</p>
      <p>Nullam dictum felis eu pede mollis pretium. Integer tincidunt. Cras dapibus. Vivamus elementum semper nisi. Aenean vulputate eleifend tellus. Aenean leo ligula, porttitor eu, consequat vitae, eleifend ac, enim. Aliquam lorem ante, dapibus in, viverra quis, feugiat a, tellus. Phasellus viverra nulla ut metus varius laoreet. Quisque rutrum. Aenean imperdiet. Etiam ultricies nisi vel augue. Curabitur ullamcorper ultricies nisi. Nam eget dui. Etiam rhoncus. Maecenas tempus, tellus eget condimentum rhoncus, sem quam semper libero, sit amet adipiscing sem neque sed ipsum. Nam quam nunc, blandit vel, luctus pulvinar, hendrerit id, lorem. Maecenas nec odio et ante tincidunt tempus. Donec vitae sapien ut libero venenatis faucibus.</p>
      <p>Nullam quis ante. Etiam sit amet orci eget eros faucibus tincidunt. Duis leo. Sed fringilla mauris sit amet nibh. Donec sodales sagittis magna. Sed consequat, leo eget bibendum sodales, augue velit cursus nunc,</p>
      <p style="margin-bottom:0">Mit freundlichen Grüßen</p>
      <span class="signature" role="img" aria-label="Handwritten signature of Carola Wendtke"></span>
    </div>

    <div class="footer">Lindenhofweg 14 | 45127 Essen | 0171 / 48 6 21 07 | schwungrad@carola-wendtke.de<br>Nordbank | IBAN: DE00 1000 0000 0000 1000 00 | BIC: BC10001000 | Steuer-Nr.: xxx/xxxx/xxxx</div>
  </article>

  <article class="sheet sheet--small">
    <div class="sheet-decor" role="img" aria-label="Faint grey background decoration area"></div>
    <div class="sheet-mark"></div>
    <div class="sheet-name">Carola Wendtke</div>
    <div class="sheet-tagline">Die Schwungrad-Lotsin</div>

    <div class="sender">Carola Wendtke | Lindenhofweg 14 | 45127 Essen</div>
    <div class="contact">Mobil 0171 / 48 6 21 07<br>schwungrad@carola-wendtke.de<br>Steuernummer: xxx/xxxx/xxxx</div>
    <span class="fold fold--one"></span>
    <span class="fold fold--two"></span>

    <div class="footer">Lindenhofweg 14 | 45127 Essen | 0171 / 48 6 21 07 | schwungrad@carola-wendtke.de<br>Nordbank | IBAN: DE00 1000 0000 0000 1000 00 | BIC: BC10001000 | Steuer-Nr.: xxx/xxxx/xxxx</div>
  </article>

</section>

</body>
</html>
```